Custom Manufacturing Job Shop

We are looking for a business card design for Tall Oak Fabrication Inc. Tall Oak is a family owned business that manufactures any custom product to fit a customers needs, whether it is custom 1 piece or production parts, we truly take on projects that others just cant do. to help in your design go to www.talloakfab.example for a more in depth idea. we have the following capabilities that we would like to see on the card somewhere...maybe on the back of a 2 sided card? we are fully open to ideas.
Machining
• Fabrication
• Millwork
• Maintenance
• Laser Cutting
• Precision Forming
Engineering
Blasting/Painting

No matter how big or small, We literally do it all

preferably black or darker cards but we don't mind to see some color if you see a better fit. we are interested in looking at anything that catches attention.
I have attached our logo, if it is needed in a different file type please let me know and I will send it to you if I can. maybe adding some type of drawing or dimensional lines would be something to add?? just throwing ideas out there....

Reason: I added one of our shredder designs and would like to see a few more cards if possible using this. any questions please don't hesitate to ask!!

Target Market(s)

anyone looking for design/manufacturing/machining whether it is custom 1 off parts or production.

Industry/Entity Type

Business

Contact Information for Business Card

preferably darker shades, but also not opposed to some color in the same sense....not too bright

Font styles to use
Serif
Sans Serif

Requirements
Must have
• Dell Marwick
• Direct:555-213-7790
• Cell:555-348-1162
• Fax: 555-907-4425
• 42 Quarry Lane
• Klingerstown, PA 00000
• I also would request having it in a format I can give to the company making the business cards to edit names/numbers etc. for the entire staff.
Nice to have
• drafting lines? we are open to almost anything....
Should not have
• exotic colors

```html
<!DOCTYPE html>
<html lang="en">
<head>
<meta charset="utf-8">
<title>Tall Oak Fabrication Inc. – Business Card</title>
<link rel="stylesheet" href="https://fonts.googleapis.com/css2?family=Exo+2:wght@400;500;600;800&display=swap">
<style>
  :root {
    --page-bg: #e9e9e9;
    --band-dark: #5b5b5b;
    --band-mid: #b4b4b4;
    --band-soft: #d8d8d8;
    --ink-dark: #4a4a4a;
    --ink-light: #ffffff;
  }
  * { margin: 0; padding: 0; box-sizing: border-box; }
  html, body {
    width: 1200px; height: 900px; overflow: hidden;
    background: var(--page-bg);
    font-family: "Exo 2", sans-serif;
  }
  .card {
    position: absolute; left: 100px; top: 165px;
    width: 1000px; height: 570px;
    border-radius: 48px; overflow: hidden;
    box-shadow: 0 14px 40px rgba(0,0,0,0.18);
  }
  .card-art { position: absolute; inset: 0; }
  .brand {
    position: absolute; left: 90px; top: 140px;
    display: flex; align-items: center; gap: 14px;
  }
  .brand-dot {
    width: 30px; height: 30px; border-radius: 50%;
    background: var(--ink-dark);
  }
  .brand-name {
    font-weight: 800; font-size: 58px; letter-spacing: 2px;
    color: var(--ink-dark); text-transform: uppercase;
  }
  .person {
    position: absolute; left: 190px; top: 250px; text-align: center;
    color: var(--ink-dark);
  }
  .person-name { font-weight: 600; font-size: 26px; letter-spacing: 1px; text-transform: uppercase; }
  .person-title { font-weight: 500; font-size: 19px; }
  .contact {
    position: absolute; right: 40px; top: 215px;
    list-style: none; color: var(--ink-light);
    font-size: 19px; letter-spacing: 1px;
  }
  .contact li {
    display: flex; justify-content: flex-end; align-items: center;
    gap: 12px; height: 32px;
  }
  .contact svg { width: 20px; height: 20px; fill: var(--ink-light); }
  .address {
    position: absolute; left: 60px; top: 470px;
    color: var(--ink-light); font-size: 22px; font-weight: 500; line-height: 1.45;
    letter-spacing: 0.5px;
  }
</style>
</head>
<body>
<div class="card">
  <svg class="card-art" viewBox="0 0 1000 570" preserveAspectRatio="none" aria-hidden="true">
    <defs>
      <linearGradient id="lightFace" x1="0" y1="0" x2="0" y2="1">
        <stop offset="0" stop-color="#f4f4f4"/>
        <stop offset="1" stop-color="#ffffff"/>
      </linearGradient>
    </defs>
    <rect width="1000" height="570" fill="url(#lightFace)"/>
    <path d="M0,360 C200,430 420,380 560,290 C700,200 840,110 1000,100 L1000,570 L0,570 Z" fill="var(--band-soft)"/>
    <path d="M0,378 C200,448 420,398 560,308 C700,218 840,128 1000,118 L1000,570 L0,570 Z" fill="var(--band-mid)"/>
    <path d="M0,390 C200,460 420,410 560,320 C700,230 840,140 1000,130 L1000,570 L0,570 Z" fill="#ffffff"/>
    <path d="M0,400 C200,470 420,420 560,330 C700,240 840,150 1000,140 L1000,570 L0,570 Z" fill="var(--band-dark)"/>
  </svg>

  <div class="brand">
    <span class="brand-dot"></span>
    <span class="brand-name">Tall Oak</span>
  </div>

  <div class="person">
    <p class="person-name">Dell Marwick</p>
    <p class="person-title">Managing Director</p>
  </div>

  <ul class="contact">
    <li>555-213-7790
      <svg viewBox="0 0 24 24"><path d="M6.6 10.8a15 15 0 0 0 6.6 6.6l2.2-2.2c.3-.3.7-.4 1-.2 1.1.4 2.3.6 3.6.6.6 0 1 .4 1 1V20c0 .6-.4 1-1 1A17 17 0 0 1 3 4c0-.6.4-1 1-1h3.5c.6 0 1 .4 1 1 0 1.3.2 2.5.6 3.6.1.3 0 .7-.2 1z"/></svg>
    </li>
    <li>555-348-1162
      <svg viewBox="0 0 24 24"><path d="M7 1h10a2 2 0 0 1 2 2v18a2 2 0 0 1-2 2H7a2 2 0 0 1-2-2V3a2 2 0 0 1 2-2zm0 3v14h10V4zm5 15.2a1.2 1.2 0 1 0 0 2.4 1.2 1.2 0 0 0 0-2.4z"/></svg>
    </li>
    <li>555-907-4425
      <svg viewBox="0 0 24 24"><path d="M6 2h9l3 3v5H6zM3 11h18a1 1 0 0 1 1 1v9a1 1 0 0 1-1 1H3a1 1 0 0 1-1-1v-9a1 1 0 0 1 1-1zm3 3v2h3v-2zm5 0v2h3v-2zm-5 4v2h3v-2zm5 0v2h3v-2z"/></svg>
    </li>
    <li>dell@talloakfab.example
      <svg viewBox="0 0 24 24"><path d="M2 5h20v14H2zm2 2v.5l8 5.5 8-5.5V7zm0 2.9V17h16V9.9l-8 5.5z"/></svg>
    </li>
    <li>www.talloakfab.example
      <svg viewBox="0 0 24 24"><path d="M12 2a10 10 0 1 0 0 20 10 10 0 0 0 0-20zm6.9 9h-3a15 15 0 0 0-1.3-6A8 8 0 0 1 18.9 11zM12 4.1c.9 1.3 1.7 3.7 1.900 6.9h-3.8c.2-3.2 1-5.6 1.9-6.9zM9.4 5a15 15 0 0 0-1.3 6h-3A8 8 0 0 1 9.4 5zM5.1 13h3a15 15 0 0 0 1.3 6A8 8 0 0 1 5.1 13zm6.9 6.9c-.9-1.3-1.7-3.7-1.9-6.9h3.8c-.2 3.2-1 5.6-1.9 6.9zm2.6-.9a15 15 0 0 0 1.3-6h3a8 8 0 0 1-4.300 6z"/></svg>
    </li>
  </ul>

  <p class="address">42 Quarry Lane<br>Klingerstown, PA 00000</p>
</div>
</body>
</html>
```